To revamp/upgrade company website

We recently changed our company core values and mission statement, I have added this (very simply) via word press. However I would like the values and mission statement page design upgrading and also to have them run through the rest of the website pages. Also, open to other recommendations on how to update our website. The main take away from the website should be that we are the "people company", both for our customers and our staff. We would like the logo and colour theme to remain as is. Calderwick Healthcare is a health and social care company, who privately own a group of care homes in the north west of england. Attached is the core values, PEOPLE, our mission statement and also a word cloud that we would also like to embed in to the website.

```html
<!DOCTYPE html>
<html lang="en">
<head>
<meta charset="utf-8">
<title>Calderwick Healthcare – Website Pages</title>
<link rel="stylesheet" href="https://fonts.googleapis.com/css2?family=Inter:wght@400;500;600;700&family=Open+Sans:wght@400;600;700&display=swap">
<style>
:root{
  --board:#6b6b6b;
  --white:#ffffff;
  --ink:#1d2433;
  --muted:#4b5563;
  --navy:#2f4a6b;
  --badge:#3b5273;
  --footer:#131c36;
  --accent:#ef8a63;
  --line:#e7ebf1;
  --soft:#f6f8fb;
  --tint:#eef3f8;
  --note:#f6f1e6;
}
*{box-sizing:border-box;margin:0;padding:0}
html,body{width:1200px;height:1161px;overflow:hidden;background:var(--board)}
body{position:relative;font-family:"Inter",sans-serif;color:var(--ink)}
.page{position:absolute;background:var(--white);overflow:hidden;box-shadow:0 2px 6px rgba(0,0,0,.25)}
.page *{position:absolute}
.page p *,.page li,.page li *,.page .sub-bar *,.page .brand *{position:static}
.page-home{left:43px;top:39px;width:543px;height:639px}
.page-about{left:614px;top:39px;width:543px;height:336px}
.page-mission{left:614px;top:404px;width:543px;height:510px}
.page-contact{left:43px;top:706px;width:543px;height:415px}

/* main header */
.main-header{left:0;top:0;width:543px;height:28px;background:var(--white)}
.brand{font-weight:700;color:var(--navy);white-space:nowrap;display:flex;align-items:center;gap:3px}
.brand-mark{display:inline-block;background:var(--navy)}
.main-header .brand{left:6px;top:6px;font-size:13px}
.main-header .brand-mark{width:9px;height:9px}
.main-nav{left:221px;top:10px;display:flex;gap:13.5px;font-size:4.9px;color:var(--ink)}
.main-nav span{position:static}
.nav-cta{left:492px;top:8px;width:43px;height:12px;background:var(--navy);color:#fff;font-size:4.9px;font-weight:600;display:flex;align-items:center;justify-content:center;transform:skewX(-18deg)}
.nav-cta span{position:static;transform:skewX(18deg)}

/* hero */
.hero{left:0;top:28px;width:543px;height:242px;background:linear-gradient(90deg,#5d6e73 0%,#8b9390 30%,#c9bba8 55%,#e3d3c2 75%,#b9a793 100%)}
.hero-shade{left:0;top:28px;width:300px;height:242px;background:linear-gradient(90deg,rgba(40,52,60,.45),rgba(40,52,60,0))}
.hero-title{left:26px;top:62px;font-family:"Open Sans",sans-serif;font-weight:700;font-size:29px;line-height:33px;color:#fff}
.hero-sub{left:26px;top:138px;width:170px;font-family:"Open Sans",sans-serif;font-size:13px;line-height:17px;color:#fff}
.hero-cta{left:30px;top:204px;width:100px;height:22px;background:var(--navy);transform:skewX(-18deg);display:flex;align-items:center;justify-content:center}
.hero-cta span{position:static;transform:skewX(18deg);color:#fff;font-size:10px;font-weight:600;letter-spacing:.2px}

/* sub header */
.sub-header{left:0;top:0;width:543px;height:18px;background:var(--white);border-bottom:1px solid var(--line)}
.sub-bar{top:3px;display:flex;align-items:center;gap:4px;white-space:nowrap}
.sub-bar .brand{font-size:7.5px}
.sub-bar .brand-mark{width:5px;height:5px}
.sub-bar .site-name{font-size:4.5px;font-weight:600;margin-left:1px}
.sub-nav{display:flex;gap:2.5px;font-size:4.5px;font-weight:600;margin-left:2px}
.sub-nav .active{color:#5a78a0}
.intro{left:0;top:18px;width:543px;height:66px;background:linear-gradient(180deg,#f4f6fa,#ffffff)}
.eyebrow{top:37px;font-size:4.4px;font-weight:600;letter-spacing:.6px;color:var(--navy);display:flex;align-items:center;gap:3px}
.eyebrow i{position:static;display:inline-block;width:7px;height:1px;background:var(--accent)}
.page-title{top:43px;font-size:12.4px;font-weight:600;color:var(--ink);white-space:nowrap}
.page-lede{top:60px;font-size:4.3px;color:var(--muted);padding-left:6px;border-left:1px solid var(--accent);line-height:6px;white-space:nowrap}

/* headings & copy */
.section-title{font-size:6.8px;font-weight:600}
.small-title{font-size:5.2px;font-weight:600}
.copy{font-size:4.3px;line-height:5.4px;color:var(--muted)}
.box{border:1px solid var(--line);border-radius:4px;background:var(--white)}
.list{font-size:4.3px;line-height:5.4px;color:var(--muted);padding-left:11px}

/* value cards */
.value{width:58px;height:54px;border:1px solid #f0f2f5;border-radius:4px;background:linear-gradient(180deg,#fff,#fafbfc)}
.value.short{height:43px}
.value b{left:5px;top:5px;width:11px;height:11px;border-radius:2px;background:var(--badge);color:#fff;font-size:7px;font-weight:700;display:flex;align-items:center;justify-content:center}
.value h4{left:5px;top:20px;font-size:5.2px;font-weight:600;color:var(--ink)}
.value p{left:5px;top:27px;width:48px;font-size:4.1px;line-height:5.1px;color:var(--muted)}

/* buttons */
.slant-btn{background:var(--navy);transform:skewX(-18deg);display:flex;align-items:center;justify-content:center}
.slant-btn span{position:static;transform:skewX(18deg);color:#fff;font-size:6px;font-weight:500}
.pill-btn{background:var(--navy);color:#fff;border-radius:6px;font-size:4.2px;font-weight:600;display:flex;align-items:center;justify-content:center}

/* word cloud frame */
.cloud-well{background:var(--tint);border-radius:2px}
.cloud-frame{background:#fff;border:1px solid #cfd7e2;border-radius:3px}
.cloud-area{background:var(--soft);border:1px solid #e2e7ee}
.tiny{font-size:2px;color:#6b7280;white-space:nowrap}

/* form */
.field-label{font-size:4.3px;color:var(--ink)}
.field{border:1px solid var(--line);border-radius:2px;background:#fff}
.note{background:linear-gradient(90deg,var(--note),#eef2f1);border-radius:3px;font-size:4.3px;color:var(--ink);display:flex;align-items:center;padding-left:6px;padding-right:6px}

/* footer */
.site-footer{left:0;width:543px;height:86px;background:var(--footer);color:#fff}
.site-footer .f-title{top:12px;font-size:4.5px;font-weight:600}
.site-footer .f-text{top:21px;font-size:4.3px;line-height:5.3px;color:#dde3ee}
.site-footer .f-text b{color:#fff}
.site-footer .f-list{top:21px;font-size:4.3px;line-height:7.7px;color:#dde3ee;padding-left:11px}
.site-footer .pills{top:43px;left:73px;display:flex;gap:2px}
.site-footer .pill{position:static;background:#fff;color:#b9c2cf;border-radius:6px;font-size:3.6px;height:11px;padding:0 4px;display:flex;align-items:center;gap:2px;white-space:nowrap}
.site-footer .pill i{position:static;display:inline-block;width:2px;height:2px;border-radius:50%;background:#8792a3}
.site-footer .rule{top:71px;left:73px;width:396px;height:1px;background:#27304b}
.site-footer .legal{top:76px;left:73px;font-size:4.1px;color:#c8cfdb}
.site-footer .legal strong{color:#fff}
.site-footer .made{top:76px;left:431px;font-size:4.1px;color:#c8cfdb}
</style>
</head>
<body>

<!-- Home page -->
<section class="page page-home">
  <header class="main-header">
    <div class="brand"><i class="brand-mark"></i>Calderwick</div>
    <nav class="main-nav"><span>Home</span><span>About Us</span><span>Live With Us</span><span>How We Care</span><span>Help &amp; Support</span><span>Work With Us</span><span>FAQs</span></nav>
    <div class="nav-cta"><span>Contact Us</span></div>
  </header>
  <div class="hero" role="img" aria-label="Photograph of a smiling older resident with a caring staff member's hands on her shoulders"></div>
  <div class="hero-shade"></div>
  <h1 class="hero-title">Putting Our<br>People First</h1>
  <p class="hero-sub">Creating a culture of excellence in delivering health care</p>
  <div class="hero-cta"><span>GET IN TOUCH</span></div>

  <h2 class="section-title" style="left:79px;top:289px">Our PEOPLE values</h2>
  <p class="copy" style="left:79px;top:311px">These values guide how we show up for residents, families, colleagues and our community every day.</p>

  <div class="value" style="left:79px;top:329px"><b>P</b><h4>Purpose</h4><p>We enrich lives and make a meaningful difference every day.</p></div>
  <div class="value" style="left:144px;top:329px"><b>E</b><h4>Excellence</h4><p>We create an environment where residents and staff can thrive.</p></div>
  <div class="value" style="left:209px;top:329px"><b>O</b><h4>Openness</h4><p>We build trust with honest, respectful communication and feedback.</p></div>
  <div class="value" style="left:274px;top:329px"><b>P</b><h4>Passion</h4><p>We take pride in delivering exceptional care that makes a real difference.</p></div>
  <div class="value" style="left:339px;top:329px"><b>L</b><h4>Learning</h4><p>We grow through development, reflection and shared knowledge.</p></div>
  <div class="value" style="left:405px;top:329px"><b>E</b><h4>Empathy</h4><p>We listen to understand the unique needs of others.</p></div>

  <h2 class="section-title" style="left:79px;top:454px">Our mission</h2>
  <p class="copy" style="left:79px;top:467px;width:182px;padding-left:6px;border-left:1px solid var(--accent)">“Our daily mission is to make each moment meaningful for us and for those around us through acts of kindness, integrity, and connection...”</p>
  <div class="slant-btn" style="left:77px;top:482px;width:79px;height:13px"><span>Read the full mission</span></div>

  <div class="box" style="left:275px;top:409px;width:189px;height:124px"></div>
  <div class="cloud-well" style="left:280px;top:414px;width:178px;height:104px"></div>
  <div class="cloud-frame" style="left:287px;top:421px;width:165px;height:90px"></div>
  <div class="cloud-area" style="left:293px;top:430px;width:153px;height:64px"></div>
  <span class="tiny" style="left:293px;top:497px">Place your word cloud image or embed here.</span>
  <p class="copy" style="left:280px;top:521px">We can embed your official word cloud here.</p>

  <footer class="site-footer" style="top:554px">
    <span class="f-title" style="left:73px">Calderwick Healthcare</span>
    <p class="f-text" style="left:73px;width:140px">We are the <b>people company</b> — putting residents, families and staff first across our care homes in the North West of England.</p>
    <span class="f-title" style="left:224px">Company</span>
    <ul class="f-list" style="left:224px"><li>Mission &amp; Values</li><li>About</li><li>Contact</li></ul>
    <span class="f-title" style="left:350px">Get in touch</span>
    <ul class="f-list" style="left:350px"><li>Email: info@calderwickhealthcare.co.uk</li><li>Phone: +44 0000 000000</li><li>North West England</li></ul>
    <div class="pills"><span class="pill"><i></i>Person-centred care</span><span class="pill"><i></i>Dignity &amp; respect</span></div>
    <div class="rule"></div>
    <p class="legal">© <strong>Calderwick Healthcare</strong>. All rights reserved.</p>
    <p class="made">Made with care.</p>
  </footer>
</section>

<!-- About page -->
<section class="page page-about">
  <div class="intro"></div>
  <header class="sub-header">
    <div class="sub-bar" style="left:79px">
      <div class="brand"><i class="brand-mark"></i>Calderwick</div>
      <span class="site-name">Calderwick Healthcare</span>
      <nav class="sub-nav"><span>Home</span><span>Mission &amp; Values</span><span class="active">About</span><span>Contact</span></nav>
    </div>
  </header>
  <p class="eyebrow" style="left:79px"><i></i>ABOUT CALDERWICK</p>
  <h1 class="page-title" style="left:79px">Privately owned care homes across the North West of England</h1>
  <p class="page-lede" style="left:79px">We create safe, caring environments where residents feel at home and staff feel supported to grow.</p>

  <div class="box" style="left:79px;top:101px;width:189px;height:39px"></div>
  <h3 class="small-title" style="left:85px;top:108px">Who we are</h3>
  <p class="copy" style="left:85px;top:116px;width:178px">Calderwick Healthcare is committed to compassionate, person-centred care that respects dignity and celebrates life stories. We’re proud to be known as the <b>people company</b> for our residents, families and colleagues.</p>

  <div class="box" style="left:275px;top:101px;width:189px;height:47px"></div>
  <h3 class="small-title" style="left:281px;top:108px">What we stand for</h3>
  <p class="copy" style="left:281px;top:116px;width:178px">Our PEOPLE values guide daily decisions and behaviours — shaping culture, leadership and the quality of care.</p>
  <div class="pill-btn" style="left:281px;top:129px;width:65px;height:12px">Explore Mission &amp; Values</div>

  <div class="box" style="left:74px;top:179px;width:395px;height:43px"></div>
  <h3 class="small-title" style="left:80px;top:186px">Our approach</h3>
  <ul class="list" style="left:80px;top:196px"><li>Relationship-centred care and meaningful moments</li><li>Open communication with families and partners</li><li>Continuous learning and development for our teams</li></ul>

  <footer class="site-footer" style="top:250px">
    <span class="f-title" style="left:73px">Calderwick Healthcare</span>
    <p class="f-text" style="left:73px;width:140px">We are the <b>people company</b> — putting residents, families and staff first across our care homes in the North West of England.</p>
    <span class="f-title" style="left:224px">Company</span>
    <ul class="f-list" style="left:224px"><li>Mission &amp; Values</li><li>About</li><li>Contact</li></ul>
    <span class="f-title" style="left:350px">Get in touch</span>
    <ul class="f-list" style="left:350px"><li>Email: info@calderwickhealthcare.co.uk</li><li>Phone: +44 0000 000000</li><li>North West England</li></ul>
    <div class="pills"><span class="pill"><i></i>Person-centred care</span><span class="pill"><i></i>Dignity &amp; respect</span></div>
    <div class="rule"></div>
    <p class="legal">© <strong>Calderwick Healthcare</strong>. All rights reserved.</p>
    <p class="made">Made with care.</p>
  </footer>
</section>

<!-- Mission & values page -->
<section class="page page-mission">
  <div class="intro"></div>
  <header class="sub-header">
    <div class="sub-bar" style="left:79px">
      <div class="brand"><i class="brand-mark"></i>Calderwick</div>
      <span class="site-name">Calderwick Healthcare</span>
      <nav class="sub-nav"><span>Home</span><span class="active">Mission &amp; Values</span><span>About</span><span>Contact</span></nav>
    </div>
  </header>
  <p class="eyebrow" style="left:79px"><i></i>MISSION &amp; VALUES</p>
  <h1 class="page-title" style="left:79px">Embedding our PEOPLE values across everything we do</h1>
  <p class="page-lede" style="left:79px">This page is designed to be reused across the site so the message is consistent on every page.</p>

  <div class="box" style="left:79px;top:101px;width:226px;height:78px"></div>
  <h3 class="section-title" style="left:85px;top:112px">Our mission</h3>
  <p class="copy" style="left:85px;top:123px;width:214px">Our daily mission is to make each moment meaningful for us and for those around us through acts of kindness, integrity, and connection. We provide compassionate, person-centred care that honours the lives and legacies of our residents and their families, while fostering a culture where our staff feel empowered, valued, and inspired to grow.</p>
  <div class="note" style="left:85px;top:150px;width:214px;height:21px;line-height:5.4px">Care is a relationship, not a transaction. Every resident is someone’s family. Every staff member deserves an environment where they can thrive and lead with empathy.</div>

  <div class="box" style="left:313px;top:101px;width:151px;height:110px"></div>
  <h3 class="small-title" style="left:319px;top:108px">Values word cloud</h3>
  <div class="cloud-well" style="left:319px;top:115px;width:139px;height:82px"></div>
  <div class="cloud-frame" style="left:324px;top:120px;width:130px;height:72px"></div>
  <div class="cloud-area" style="left:329px;top:126px;width:120px;height:51px"></div>
  <span class="tiny" style="left:329px;top:180px">Place your word cloud here.</span>
  <p class="copy" style="left:319px;top:199px">Replace with your official word-cloud image or embed code.</p>

  <h2 class="section-title" style="left:79px;top:249px">PEOPLE values</h2>
  <div class="value" style="left:79px;top:262px"><b>P</b><h4>Purpose</h4><p>We enrich lives, honour legacies and make a meaningful difference every day.</p></div>
  <div class="value" style="left:144px;top:262px"><b>E</b><h4>Excellence</h4><p>We hold ourselves to the highest standards so residents and staff can thrive.</p></div>
  <div class="value" style="left:209px;top:262px"><b>O</b><h4>Openness</h4><p>We build trust through honest, respectful communication and feedback.</p></div>
  <div class="value" style="left:274px;top:262px"><b>P</b><h4>Passion</h4><p>We are proud of the real difference our care makes in people’s lives.</p></div>
  <div class="value" style="left:339px;top:262px"><b>L</b><h4>Learning</h4><p>We empower growth through development, reflection and shared knowledge.</p></div>
  <div class="value" style="left:405px;top:262px"><b>E</b><h4>Empathy</h4><p>We actively listen and seek to understand the unique needs of others.</p></div>

  <div class="box" style="left:74px;top:348px;width:395px;height:49px"></div>
  <h3 class="small-title" style="left:80px;top:355px">How we embed this across the website</h3>
  <ul class="list" style="left:80px;top:366px"><li>Reusable PEOPLE strip: include the six value pills at the end of key pages.</li><li>People-first copy: use inclusive, resident- and staff-centred language on every page.</li><li>Design accents: subtle gradient highlights and accessible contrasts.</li><li>Photography guidance: real interactions, dignity and warmth over stock poses.</li></ul>

  <footer class="site-footer" style="top:425px">
    <span class="f-title" style="left:73px">Calderwick Healthcare</span>
    <p class="f-text" style="left:73px;width:140px">We are the <b>people company</b> — putting residents, families and staff first across our care homes in the North West of England.</p>
    <span class="f-title" style="left:224px">Company</span>
    <ul class="f-list" style="left:224px"><li>Mission &amp; Values</li><li>About</li><li>Contact</li></ul>
    <span class="f-title" style="left:350px">Get in touch</span>
    <ul class="f-list" style="left:350px"><li>Email: info@calderwickhealthcare.co.uk</li><li>Phone: +44 0000 000000</li><li>North West England</li></ul>
    <div class="pills"><span class="pill"><i></i>Person-centred care</span><span class="pill"><i></i>Dignity &amp; respect</span></div>
    <div class="rule"></div>
    <p class="legal">© <strong>Calderwick Healthcare</strong>. All rights reserved.</p>
    <p class="made">Made with care.</p>
  </footer>
</section>

<!-- Contact page -->
<section class="page page-contact">
  <div class="intro"></div>
  <header class="sub-header">
    <div class="sub-bar" style="left:80px">
      <div class="brand"><i class="brand-mark"></i>Calderwick</div>
      <span class="site-name">Calderwick Healthcare</span>
      <nav class="sub-nav"><span>Home</span><span>Mission &amp; Values</span><span>About</span><span class="active">Contact</span></nav>
    </div>
  </header>
  <p class="eyebrow" style="left:80px"><i></i>CONTACT</p>
  <h1 class="page-title" style="left:80px">We’re here to help</h1>
  <p class="page-lede" style="left:80px">Get in touch to learn more about our homes, our approach and how we can support your family.</p>

  <div class="box" style="left:80px;top:102px;width:187px;height:121px"></div>
  <h3 class="small-title" style="left:86px;top:110px">Send us a message</h3>
  <span class="field-label" style="left:86px;top:117px">Full name</span>
  <div class="field" style="left:86px;top:123px;width:175px;height:11px"></div>
  <span class="field-label" style="left:86px;top:139px">Email</span>
  <div class="field" style="left:86px;top:145px;width:175px;height:11px"></div>
  <span class="field-label" style="left:86px;top:162px">Message</span>
  <div class="field" style="left:86px;top:168px;width:175px;height:34px"></div>
  <div class="pill-btn" style="left:86px;top:208px;width:21px;height:11px">Send</div>

  <div class="box" style="left:276px;top:102px;width:187px;height:121px"></div>
  <h3 class="small-title" style="left:282px;top:110px">Contact details</h3>
  <p class="copy" style="left:282px;top:117px;line-height:7.2px;color:var(--ink)">Email: info@calderwickhealthcare.co.uk<br>Phone: +44 0000 000000<br>Location: North West England</p>
  <div class="note" style="left:282px;top:138px;width:175px;height:16px">Prefer email? We aim to respond within one business day.</div>

  <h2 class="small-title" style="left:80px;top:254px">Our PEOPLE values</h2>
  <div class="value short" style="left:80px;top:266px"><b>P</b><h4>Purpose</h4><p>Enrich lives daily.</p></div>
  <div class="value short" style="left:145px;top:266px"><b>E</b><h4>Excellence</h4><p>High standards, thriving people.</p></div>
  <div class="value short" style="left:210px;top:266px"><b>O</b><h4>Openness</h4><p>Honest, respectful communication.</p></div>
  <div class="value short" style="left:275px;top:266px"><b>P</b><h4>Passion</h4><p>Proud to make a difference.</p></div>
  <div class="value short" style="left:340px;top:266px"><b>L</b><h4>Learning</h4><p>Grow, reflect, share.</p></div>
  <div class="value short" style="left:406px;top:266px"><b>E</b><h4>Empathy</h4><p>Listen to understand.</p></div>

  <footer class="site-footer" style="top:329px">
    <span class="f-title" style="left:73px">Calderwick Healthcare</span>
    <p class="f-text" style="left:73px;width:140px">We are the <b>people company</b> — putting residents, families and staff first across our care homes in the North West of England.</p>
    <span class="f-title" style="left:224px">Company</span>
    <ul class="f-list" style="left:224px"><li>Mission &amp; Values</li><li>About</li><li>Contact</li></ul>
    <span class="f-title" style="left:350px">Get in touch</span>
    <ul class="f-list" style="left:350px"><li>Email: info@calderwickhealthcare.co.uk</li><li>Phone: +44 0000 000000</li><li>North West England</li></ul>
    <div class="pills"><span class="pill"><i></i>Person-centred care</span><span class="pill"><i></i>Dignity &amp; respect</span></div>
    <div class="rule"></div>
    <p class="legal">© <strong>Calderwick Healthcare</strong>. All rights reserved.</p>
    <p class="made">Made with care.</p>
  </footer>
</section>

</body>
</html>
```